Roving Rotor Crew Van Wrap Project

In our busy world, you don’t have time to sit in a mechanic’s garage for hours to get your brakes replaced and you probably don’t want to deal with the inconvenience of dropping off a car, arranging rides, and being without a vehicle for a day or more. we’ve worked hard to create a convenient, affordable service designed to save you time and money.

Industry/Entity Type

Mechanic

Font styles to use
Sans Serif

Colors

Designer to choose colors to be used in the design.

Requirements
Must have
• 888-517-3962
• www.rovingrotorcrew.example
• We Come To You Home or Business
• Full Brake Service Repair
Should not have
• Don't want to wrap the whole vehicle. Want to just put letters and logo

```html
<!DOCTYPE html>
<html lang="en">
<head>
<meta charset="utf-8">
<title>Roving Rotor Crew – Van Wrap</title>
<link href="https://fonts.googleapis.com/css2?family=Oswald:wght@500;600;700&family=Open+Sans:wght@700&display=swap" rel="stylesheet">
<style>
  :root {
    --wrap-red: #c8111e;
    --wrap-navy: #1b2d45;
    --wrap-tan: #d8ae78;
    --wrap-white: #ffffff;
    --page-bg: #ffffff;
  }
  html, body {
    margin: 0;
    padding: 0;
    width: 1200px;
    height: 502px;
    overflow: hidden;
    background: var(--page-bg);
  }
  .wrap-layout {
    display: block;
    width: 1200px;
    height: 502px;
  }
  .rear-panel { fill: var(--wrap-tan); }
  .rear-accent { fill: var(--wrap-red); }
  .brand-name {
    font-family: "Oswald", sans-serif;
    font-weight: 700;
    font-size: 21px;
    fill: var(--wrap-navy);
  }
  .tagline-lead {
    font-family: "Oswald", sans-serif;
    font-weight: 600;
    font-size: 23px;
    fill: var(--wrap-red);
  }
  .tagline-main {
    font-family: "Oswald", sans-serif;
    font-weight: 700;
    font-size: 33px;
    fill: var(--wrap-navy);
  }
  .service-band { fill: var(--wrap-red); }
  .contact-band { fill: var(--wrap-navy); }
  .service-text {
    font-family: "Oswald", sans-serif;
    font-weight: 700;
    font-size: 29px;
    fill: var(--wrap-white);
  }
  .phone-number {
    font-family: "Open Sans", sans-serif;
    font-weight: 700;
    font-size: 40px;
    fill: var(--wrap-white);
  }
  .phone-icon-ring { fill: none; stroke: var(--wrap-white); stroke-width: 2; }
  .phone-icon { fill: var(--wrap-white); }
  .web-address {
    font-family: "Open Sans", sans-serif;
    font-weight: 700;
    font-size: 12px;
    fill: var(--wrap-red);
  }
  .web-icon { fill: var(--wrap-red); }
</style>
</head>
<body>
<svg class="wrap-layout" viewBox="0 0 1200 502" xmlns="http://www.w3.org/2000/svg">
  <!-- rear door panel -->
  <path class="rear-panel" d="M160 82 Q166 52 205 50 L332 50 Q372 110 370 190 Q368 250 342 300 L160 330 Z"/>
  <path class="rear-accent" d="M332 50 L356 50 Q396 112 393 190 Q390 255 362 298 L342 300 Q368 250 370 190 Q372 110 332 50 Z"/>

  <!-- brand name -->
  <text class="brand-name" x="264" y="198" text-anchor="middle">ROVING ROTOR CREW</text>

  <!-- tagline -->
  <text class="tagline-lead" x="413" y="160">WE COME TO</text>
  <text class="tagline-main" x="413" y="192">YOU HOME</text>
  <text class="tagline-main" x="413" y="225">OR BUSINESS</text>

  <!-- diagonal bands -->
  <polygon class="service-band" points="160,328 925,222 1000,240 1000,262 390,345 160,356"/>
  <polygon class="contact-band" points="390,345 1000,262 1050,290 1050,318 390,410"/>

  <text class="service-text" x="380" y="330" transform="rotate(-7.4 380 330)">FULL BRAKE SERVICE REPAIR</text>

  <!-- phone -->
  <g transform="rotate(-7.4 445 378)">
    <circle class="phone-icon-ring" cx="445" cy="378" r="16"/>
    <path class="phone-icon" d="M439 370 l4 -1 l2 5 l-2 2 q2 4 6 6 l2 -2 l5 2 l-1 4 q-10 1 -16 -16 z"/>
  </g>
  <text class="phone-number" x="478" y="388" transform="rotate(-7.4 478 388)">888-517-3962</text>

  <!-- web -->
  <circle class="web-icon" cx="611" cy="393" r="6"/>
  <text class="web-address" x="622" y="396" transform="rotate(-7.4 622 396)">www.rovingrotorcrew.example</text>
</svg>
</body>
</html>
```